Just to be clear - I have the domain and the wordpress site (which is messy). I need someone to help me complete a simple blog design and then go into the existing wordpress site, and get rid of all the existing rubbish and set up the templates please. If we progress with design can we please be clear about additional costs upfront which, of course, I appreciate is the case.

Need a lifestyle blog. It is called brightyearsahead.com. Aimed at the older woman but needs to look fresh and young, not old fashioned. Navigation will be Home, Fashion, Feelings, Fitness, Contact. I have a logo but not sure it will work at the moment so happy with stylised words.Will have social media links.

Need homepage (not overly long) to have a main slider for pics/videos. Then the three category boxes underneath linking through to 2nd level pages containing blogs for that category and then the actual blog page. Happy to be led by expertise if this is not gonna work.

Am really looking for something clean and fresh like a Marvette type approach to be honest.

If you need any further direction please just ask - once design chosen I am looking to move quickly.

Thank you so much for looking at this brief

Target Market(s)

Women, 40 - 60 age group but with a younger outlook

Colors

Requirements
Must have
• Reflect youth, fun, bright
• Lift easily into a wordpress format
Should not have
• Old, staid, frumpy,dark

```html
<!DOCTYPE html>
<html lang="en">
<head>
<meta charset="utf-8">
<title>Bright Years Ahead</title>
<link rel="stylesheet" href="https://fonts.googleapis.com/css2?family=Lato:wght@300;400;700&family=Playfair+Display:wght@400;700&display=swap">
<style>
  :root {
    --pink: #e8657e;
    --pink-soft: #ec7d92;
    --plum: #5e3a52;
    --slate: #4b4749;
    --ink: #1f1a1c;
    --title-ink: #4a2a3a;
    --body-ink: #5a5558;
    --section-bg: #f8f8f8;
    --white: #ffffff;
    --footer-ink: #b3b0b1;
  }
  * { box-sizing: border-box; margin: 0; padding: 0; }
  html, body { width: 1200px; height: 2320px; overflow: hidden; }
  body {
    position: relative;
    background: var(--white);
    font-family: "Lato", sans-serif;
    color: var(--ink);
  }
  .top-nav {
    position: absolute; left: 0; top: 0; width: 1200px; height: 40px;
    background: var(--pink);
  }
  .nav-link {
    position: absolute; top: 0; line-height: 40px;
    transform: translateX(-50%);
    font-size: 13px; letter-spacing: 0.3px; color: var(--white);
    text-decoration: none; text-transform: uppercase;
  }
  .brand {
    position: absolute; left: 0; top: 70px; width: 1200px;
    text-align: center;
    font-family: "Playfair Display", serif; font-weight: 400;
    font-size: 40px; line-height: 1.05; color: var(--pink);
  }
  .hero {
    position: absolute; left: 121px; top: 193px; width: 958px; height: 439px;
    background: linear-gradient(100deg, #2a2422 0%, #5b4a3e 30%, #8d7461 55%, #b9a699 72%, #1d2226 100%);
  }
  .hero-caption {
    position: absolute; left: 29px; top: 146px; width: 385px; height: 148px;
    background: var(--pink);
    padding: 28px 31px;
    font-weight: 300; font-size: 37px; line-height: 1.1; color: var(--white);
  }
  .hero-dots {
    position: absolute; left: 448px; top: 407px;
    display: flex; gap: 16px;
  }
  .hero-dot { width: 17px; height: 17px; border-radius: 50%; background: var(--white); }
  .category {
    position: absolute; top: 665px; width: 296px; height: 359px;
    color: var(--white); font-family: "Playfair Display", serif;
    text-decoration: none;
  }
  .category--fashion { left: 121px; background: linear-gradient(180deg, #6a4259, var(--plum)); }
  .category--feelings { left: 451px; background: linear-gradient(180deg, var(--pink-soft), var(--pink)); }
  .category--fitness { left: 784px; background: linear-gradient(180deg, #575254, var(--slate)); }
  .category-kicker {
    position: absolute; left: 39px; top: 212px; font-size: 26px; line-height: 1;
  }
  .category-title {
    position: absolute; left: 39px; top: 240px; font-size: 58px; line-height: 1;
  }
  .news {
    position: absolute; left: 0; top: 1062px; width: 1200px; height: 960px;
    background: var(--section-bg);
  }
  .news-heading {
    position: absolute; left: 0; top: 28px; width: 1200px; text-align: center;
    font-family: "Playfair Display", serif; font-weight: 400;
    font-size: 50px; color: var(--title-ink);
  }
  .post {
    position: absolute; left: 121px; width: 958px; height: 351px;
    background: var(--white);
  }
  .post--first { top: 125px; }
  .post--second { top: 499px; }
  .post-photo { position: absolute; left: 0; top: 0; width: 250px; height: 351px; }
  .post-photo--cafe { background: linear-gradient(160deg, #5a6a6a 0%, #c7a27e 45%, #d6b892 70%, #8b7760 100%); }
  .post-photo--desk { background: linear-gradient(150deg, #e9eff0 0%, #f4f5f5 45%, #b8dfe0 75%, #e6e0d8 100%); }
  .post-body { position: absolute; left: 283px; top: 52px; width: 640px; }
  .post-date {
    font-weight: 700; font-size: 15px; color: var(--pink); letter-spacing: 0.2px;
  }
  .post-title {
    font-family: "Playfair Display", serif; font-weight: 400;
    font-size: 35px; line-height: 1.1; color: var(--ink); margin-top: 2px;
  }
  .post-text {
    font-size: 12.5px; line-height: 23px; color: var(--body-ink); margin-top: 22px;
  }
  .post-text + .post-text { margin-top: 23px; }
  .more-posts {
    position: absolute; left: 0; top: 896px; width: 1200px; text-align: center;
    font-size: 15px; color: var(--ink); text-transform: uppercase;
  }
  .follow-band {
    position: absolute; left: 0; top: 2022px; width: 1200px; height: 201px;
    background: linear-gradient(90deg, #e36a80, #e9758a 25%, #de5f78 50%, #eb7b8f 75%, #e3687f);
  }
  .follow-label {
    position: absolute; left: 466px; top: 77px;
    font-family: "Playfair Display", serif; font-size: 33px; line-height: 1; color: var(--white);
  }
  .social-dot {
    position: absolute; top: 76px; width: 38px; height: 38px; border-radius: 50%;
    background: var(--white);
  }
  .footer-nav {
    position: absolute; left: 0; top: 2250px; width: 1200px; height: 40px;
  }
  .footer-nav .nav-link { color: var(--footer-ink); font-size: 12px; }
</style>
</head>
<body>
  <nav class="top-nav">
    <a class="nav-link" style="left:314px">Home</a>
    <a class="nav-link" style="left:422px">Fashion</a>
    <a class="nav-link" style="left:541px">Feelings</a>
    <a class="nav-link" style="left:656px">Fitness</a>
    <a class="nav-link" style="left:759px">News</a>
    <a class="nav-link" style="left:873px">Contact</a>
  </nav>

  <div class="brand">Bright<br>Years Ahead</div>

  <section class="hero" role="img" aria-label="Slider photo: smiling woman with glasses in a warmly lit café">
    <div class="hero-caption">Everyday Festive Glam Look</div>
    <div class="hero-dots"><span class="hero-dot"></span><span class="hero-dot"></span><span class="hero-dot"></span></div>
  </section>

  <a class="category category--fashion" role="img" aria-label="Fashion category photo: woman seated on a stool in a light outfit">
    <span class="category-kicker">News</span>
    <span class="category-title">Fashion</span>
  </a>
  <a class="category category--feelings" role="img" aria-label="Feelings category photo: two friends blowing glitter">
    <span class="category-kicker">Improve those</span>
    <span class="category-title">Feelings</span>
  </a>
  <a class="category category--fitness" role="img" aria-label="Fitness category photo: woman outdoors in running gear">
    <span class="category-kicker">Better</span>
    <span class="category-title">Fitness</span>
  </a>

  <section class="news">
    <h2 class="news-heading">The News</h2>

    <article class="post post--first">
      <div class="post-photo post-photo--cafe" role="img" aria-label="Post photo: businesswoman leaning at a wooden café counter"></div>
      <div class="post-body">
        <p class="post-date">JANUARY 8, 2018</p>
        <h3 class="post-title">Have a successful and stylish business</h3>
        <p class="post-text">Lorem ipsum dolor sit amet, consectetuer adipiscing elit. Aenean commodo ligula eget dolor. Aenean massa. Cum sociis natoque penatibus et magnis dis parturient montes, nascetur ridiculus mus. Donec quam felis, ultricies nec, pellentesque eu, pretium quis, sem.</p>
        <p class="post-text">Nulla consequat massa quis enim. Donec pede justo, fringilla vel, aliquet nec, vulputate eget, arcu. In enim justo, rhoncus ut, imperdiet a, venenatis vitae, justo. Nullam dictum felis eu pede mollis pretium. Integer tincidunt.</p>
      </div>
    </article>

    <article class="post post--second">
      <div class="post-photo post-photo--desk" role="img" aria-label="Post photo: flat lay of accessories, glasses, tablet and stationery on a white desk"></div>
      <div class="post-body">
        <p class="post-date">JANUARY 8, 2018</p>
        <h3 class="post-title">Style and glamor in one place</h3>
        <p class="post-text">Lorem ipsum dolor sit amet, consectetuer adipiscing elit. Aenean commodo ligula eget dolor. Aenean massa. Cum sociis natoque penatibus et magnis dis parturient montes, nascetur ridiculus mus. Donec quam felis, ultricies nec, pellentesque eu, pretium quis, sem.</p>
        <p class="post-text">Nulla consequat massa quis enim. Donec pede justo, fringilla vel, aliquet nec, vulputate eget, arcu. In enim justo, rhoncus ut, imperdiet a, venenatis vitae, justo. Nullam dictum felis eu pede mollis pretium. Integer tincidunt.</p>
      </div>
    </article>

    <a class="more-posts">More post</a>
  </section>

  <section class="follow-band" role="img" aria-label="Pink-tinted strip of lifestyle photos of women">
    <span class="follow-label">Follow us</span>
    <span class="social-dot" style="left:635px" aria-label="Social link one"></span>
    <span class="social-dot" style="left:690px" aria-label="Social link two"></span>
  </section>

  <nav class="footer-nav">
    <a class="nav-link" style="left:314px">Home</a>
    <a class="nav-link" style="left:422px">Fashion</a>
    <a class="nav-link" style="left:541px">Feelings</a>
    <a class="nav-link" style="left:656px">Fitness</a>
    <a class="nav-link" style="left:759px">News</a>
    <a class="nav-link" style="left:873px">Contact</a>
  </nav>
</body>
</html>
```